whitening gel shopping website design

Hello:
We would like to create a whitening gel selling website. It will be very close to Glowbrite, but different designs. https://us.glowbriteorals.example/

What is your organization or website name?
Velvet Beaming

Industry: health and beauty
Target user: ladies between 16 to 40, please make the website friendly and lovely

website pages: main website, shop products, enrolled monthly plans, about us, contact us, policy, customer login log out, shopping cart, customer dashboard.

Website main page contains:
1. one slide show that shows advertisements.
2. show current promo codes
3.show a brief overview about our history
4. show a brief overview about the product introduction
5. show a brief overview of our monthly enrolled product plan
6. have an area to show blogs and posts (please take a look at Glowbrite home page)
7. buttons for customer to login, sign up, visit home, about us, policy, returns, subscription etc.

Note: for the contest, please finish the website main page and the product page only, now we don’t have any logo, test or images, please use yours for now.

```html
<!DOCTYPE html>
<html lang="en">
<head>
<meta charset="utf-8">
<title>Velvet Beaming — Shop</title>
<link href="https://fonts.googleapis.com/css2?family=Montserrat:wght@400;500;600;700;800&display=swap" rel="stylesheet">
<style>
  :root{
    --teal:#2a9d9a;
    --purple:#7c68ae;
    --purple-soft:#a08fcb;
    --sky:#e4f2f7;
    --ink:#333a40;
    --muted:#8a9096;
    --line:#eceef0;
    --foot:#f2f3f4;
    --white:#ffffff;
    --star:#f3c341;
    --photo-light:#fbfbfc;
    --photo-mid:#eeeff1;
    --photo-blush:#f6e9ee;
  }
  *{box-sizing:border-box;margin:0;padding:0}
  html,body{width:809px;height:1200px;overflow:hidden}
  body{font-family:"Montserrat",Arial,sans-serif;color:var(--ink);background:var(--white);position:relative}
  a{color:inherit;text-decoration:none}

  .site-header{position:absolute;left:0;top:0;width:809px;height:75px}
  .brand{position:absolute;left:22px;top:24px;font-weight:800;font-size:16px;color:var(--teal);letter-spacing:.4px}
  .subscribe-btn{position:absolute;left:612px;top:10px;width:82px;height:20px;background:var(--purple);color:var(--white);font-size:6.5px;font-weight:700;display:flex;align-items:center;justify-content:center;letter-spacing:.3px}
  .account-links{position:absolute;left:705px;top:15px;font-size:7px;color:var(--teal)}
  .main-nav{position:absolute;right:18px;top:50px;display:flex;gap:26px;font-size:7.5px;font-weight:500}
  .main-nav .active{color:var(--purple)}

  .category-bar{position:absolute;left:0;top:75px;width:809px;height:60px;background:var(--sky);display:flex;justify-content:center;gap:48px;padding-top:9px}
  .category{width:80px;display:flex;flex-direction:column;align-items:center;gap:6px;font-size:6.5px;color:var(--purple);text-transform:uppercase;font-weight:500}
  .category svg{width:24px;height:24px}

  .breadcrumb{position:absolute;left:22px;top:152px;font-size:6.5px;color:var(--muted);letter-spacing:.3px}
  .page-title{position:absolute;left:0;top:178px;width:809px;text-align:center;font-size:22px;font-weight:800;color:var(--purple);letter-spacing:1px}

  .product{position:absolute;width:186px}
  .product-photo{width:186px;height:194px;border:1px solid var(--line);
    background:radial-gradient(ellipse at 50% 55%,var(--white) 0%,var(--photo-light) 35%,var(--photo-blush) 62%,var(--photo-mid) 100%)}
  .product-name{margin-top:14px;font-size:8.5px;font-weight:500}
  .product-price{margin-top:4px;font-size:8.5px;font-weight:600}
  .add-btn{margin-top:14px;width:110px;height:27px;border:1px solid var(--teal);color:var(--teal);font-size:7px;font-weight:600;display:flex;align-items:center;justify-content:center;letter-spacing:.4px}

  .product-overlay{width:186px;height:194px;background:var(--purple);color:var(--white);padding:14px 12px;position:relative}
  .stars{color:var(--star);font-size:9px;letter-spacing:1px}
  .overlay-text{margin-top:6px;font-size:6.5px;line-height:1.5;width:150px}
  .benefits{margin-top:16px;display:grid;grid-template-columns:1fr 1fr;row-gap:14px;font-size:6.5px;text-align:center}
  .benefit{display:flex;flex-direction:column;align-items:center;gap:5px}
  .benefit svg{width:20px;height:20px}
  .benefit.wide{grid-column:1 / 3}

  .newsletter{position:absolute;left:0;top:907px;width:809px;height:98px;background:var(--teal)}
  .newsletter-text{position:absolute;left:75px;top:34px;color:var(--white);font-size:12px;line-height:1.45;width:290px}
  .email-field{position:absolute;left:398px;top:40px;width:225px;height:22px;background:var(--white);font-size:7px;color:var(--muted);padding:7px 8px}
  .submit-btn{position:absolute;left:631px;top:40px;width:110px;height:22px;background:var(--purple-soft);color:var(--white);font-size:7px;font-weight:600;display:flex;align-items:center;justify-content:center}

  .site-footer{position:absolute;left:0;top:1005px;width:809px;height:195px;background:var(--foot)}
  .footer-brand{position:absolute;left:75px;top:26px;font-weight:800;font-size:14px;color:var(--teal);letter-spacing:.4px}
  .footer-address{position:absolute;left:75px;top:70px;font-size:6.5px;line-height:1.7;color:var(--muted)}
  .footer-phone{position:absolute;left:75px;top:108px;font-size:6.5px;color:var(--muted)}
  .footer-links{position:absolute;top:33px;list-style:none;font-size:6.5px;line-height:2.1;color:var(--muted)}
  .footer-links.primary{left:306px}
  .footer-links.legal{left:475px}
  .follow{position:absolute;left:660px;top:33px;font-size:7.5px;font-weight:600;color:var(--ink);letter-spacing:.5px}
  .social{position:absolute;left:660px;top:52px;display:flex;gap:5px}
  .social span{width:14px;height:14px;border-radius:50%;background:var(--teal);display:block}
  .copyright{position:absolute;left:0;top:168px;width:809px;text-align:center;font-size:6.5px;color:var(--muted)}
</style>
</head>
<body>

<header class="site-header">
  <div class="brand">VELVET BEAMING</div>
  <a class="subscribe-btn" href="#">SUBSCRIBE NOW</a>
  <div class="account-links">Login | Signup</div>
  <nav class="main-nav">
    <a href="#">HOME</a>
    <a href="#">TEETH WHITENING KIT</a>
    <a href="#" class="active">SHOP PRODUCTS</a>
    <a href="#">ABOUT US</a>
    <a href="#">CONTACT US</a>
  </nav>
</header>

<section class="category-bar">
  <div class="category">
    <svg viewBox="0 0 24 24" fill="none" stroke="#7c68ae" stroke-width="1.2"><rect x="3" y="8" width="18" height="11" rx="2"/><path d="M8 8V5h8v3"/></svg>
    Teeth Whitening Kit
  </div>
  <div class="category">
    <svg viewBox="0 0 24 24" fill="none" stroke="#7c68ae" stroke-width="1.2"><path d="M6 4h12l-2 16H8z"/><path d="M9 20h6"/></svg>
    Toothpaste
  </div>
  <div class="category">
    <svg viewBox="0 0 24 24" fill="none" stroke="#7c68ae" stroke-width="1.2"><rect x="7" y="8" width="10" height="13" rx="2"/><rect x="9" y="3" width="6" height="5"/></svg>
    Mouthwash
  </div>
  <div class="category">
    <svg viewBox="0 0 24 24" fill="none" stroke="#7c68ae" stroke-width="1.2"><rect x="4" y="5" width="16" height="15" rx="1"/><path d="M4 10h16M8 3v4M16 3v4"/></svg>
    Product Plans
  </div>
</section>

<div class="breadcrumb">HOME &nbsp;›&nbsp; SHOP PRODUCTS</div>
<h1 class="page-title">SHOP</h1>

<article class="product" style="left:22px;top:224px">
  <div class="product-photo" role="img" aria-label="Product photo: two white day and night toothpaste tubes with pink labels"></div>
  <div class="product-name">Day and Night Toothpaste</div>
  <div class="product-price">$15.99</div>
  <a class="add-btn" href="#">ADD TO CART</a>
</article>

<article class="product" style="left:220px;top:224px">
  <div class="product-overlay">
    <div class="stars">★★★★★</div>
    <p class="overlay-text">A natural whitening paste with daily care</p>
    <div class="benefits">
      <div class="benefit">
        <svg viewBox="0 0 20 20" fill="none" stroke="#fff" stroke-width="1.2"><circle cx="10" cy="10" r="8"/><path d="M6 10l3 3 5-6"/></svg>
        Whiter Teeth
      </div>
      <div class="benefit">
        <svg viewBox="0 0 20 20" fill="none" stroke="#fff" stroke-width="1.2"><circle cx="10" cy="10" r="8"/><path d="M6 10l3 3 5-6"/></svg>
        Healthy Teeth
      </div>
      <div class="benefit wide">
        <svg viewBox="0 0 20 20" fill="none" stroke="#fff" stroke-width="1.2"><circle cx="10" cy="10" r="8"/><path d="M6 10l3 3 5-6"/></svg>
        Fresh Smelling Breath
      </div>
    </div>
  </div>
  <div class="product-name">Coconut Mouthwash</div>
  <div class="product-price">$23.99</div>
  <a class="add-btn" href="#">ADD TO CART</a>
</article>

<article class="product" style="left:417px;top:224px">
  <div class="product-photo" role="img" aria-label="Product photo: three white whitening gel refill pens"></div>
  <div class="product-name">Gel Refills</div>
  <div class="product-price">$23.99</div>
  <a class="add-btn" href="#">ADD TO CART</a>
</article>

<article class="product" style="left:612px;top:224px">
  <div class="product-photo" role="img" aria-label="Product photo: white teeth whitening kit box with LED mouthpiece"></div>
  <div class="product-name">Teeth Whitening Kit</div>
  <div class="product-price">$59.99</div>
  <a class="add-btn" href="#">ADD TO CART</a>
</article>

<article class="product" style="left:22px;top:560px">
  <div class="product-photo" role="img" aria-label="Product photo: white coconut mouthwash tube with pink label"></div>
  <div class="product-name">Coconut Mouthwash</div>
  <div class="product-price">$23.99</div>
  <a class="add-btn" href="#">ADD TO CART</a>
</article>

<article class="product" style="left:220px;top:560px">
  <div class="product-photo" role="img" aria-label="Product photo: two white day and night toothpaste tubes with pink labels"></div>
  <div class="product-name">Day and Night Toothpaste</div>
  <div class="product-price">$15.99</div>
  <a class="add-btn" href="#">ADD TO CART</a>
</article>

<article class="product" style="left:417px;top:560px">
  <div class="product-photo" role="img" aria-label="Product photo: white teeth whitening kit box with LED mouthpiece"></div>
  <div class="product-name">Teeth Whitening Kit</div>
  <div class="product-price">$59.99</div>
  <a class="add-btn" href="#">ADD TO CART</a>
</article>

<article class="product" style="left:612px;top:560px">
  <div class="product-photo" role="img" aria-label="Product photo: three white whitening gel refill pens"></div>
  <div class="product-name">Gel Refills</div>
  <div class="product-price">$23.99</div>
  <a class="add-btn" href="#">ADD TO CART</a>
</article>

<section class="newsletter">
  <p class="newsletter-text">Yes, I want to stay up-to-date with the latest Products, News and Promotion.</p>
  <div class="email-field">Email</div>
  <a class="submit-btn" href="#">SUBSCRIBE</a>
</section>

<footer class="site-footer">
  <div class="footer-brand">VELVET BEAMING</div>
  <p class="footer-address">1804 Harbor Lane<br>San Diego, CA 92101</p>
  <p class="footer-phone">1-800-555-0199</p>
  <ul class="footer-links primary">
    <li>Home</li><li>Teeth Whitening Kit</li><li>Shop Products</li><li>About Us</li><li>Contact Us</li>
  </ul>
  <ul class="footer-links legal">
    <li>Terms &amp; Conditions</li><li>Privacy Policy</li><li>Return Policy</li>
  </ul>
  <div class="follow">FOLLOW US</div>
  <div class="social" aria-label="Social links"><span></span><span></span><span></span><span></span></div>
  <div class="copyright">© 2019 Velvet Beaming</div>
</footer>

</body>
</html>
```